Plakat-Design für Tauchunternehmen im südlichen Ägypten
Zielgruppe
Wir sind ein Tauchunternehmen im südlichen Ägypten. Wir benötigen ein Plakat für die Tauchermesse, dieses soll das Herzstück werden. Ich habe noch zusätzlich ein Bild angefügt mit den Massen.
Aufgabenstellung
Die Masse sollten 95 cm breit und 245cm hoch sein. Siehe auch Bild.
Wenn möglich, wäre ein Format super, welches ich individuell drucken lassen kann in der Grösse.
Inhalt des Plakates
Sataya
Fury Shoals (Region)
Vollcharter
Liveaboard
Mini Safari
Overnight
Tagesboot
Sataya ist perfekt geeignet für Schnorcheln, Tauchen und die ganze Familie
Boote
Unsere Boote Veluna und Ostrel 1, ganz auf die Bedürfnisse von Tauchern und Schnorchler abgestimmt.
MY Ostrel 1 wurde 2021 gebaut. Mit einer Länge von 32 Meter und 8 Meter Breite bietet das aus Stahl konstruierte Boot bequem Platz für 24 Gäste.
8 Kabinen mit zwei Einzelbetten befinden sich im Unterdeck und 4 Kabinen auf dem Oberdeck.
MY Veluna wurde 2019 gebaut. Mit einer Länge von 30 Metern und einer Breite von 8 Metern bietet das aus Stahl konstruierte Boot bequem Platz für 18 Gäste.
5 Kabinen mit zwei Einzelbetten und 2 Doppelbettkabinen befinden sich im Unterdeck und 2 Einzelbettkabinen auf dem Oberdeck.
(Das folgende trifft für beide Boote zu)
Im Restaurant auf dem Hauptdeck werden 3 Buffets pro Tag serviert und auf dem grosszügigen Tauchdeck macht man sich für die Abenteuer bereit.
Auf dem Oberdeck gibt es viele schattige Sitzmöglichkeiten und eine Bar für ein gemütliches Zusammensein und zum Entspannen.
Auf dem Topdeck warten gemütliche Liegen, die ideal zum Sonne geniessen oder die Sterne beobachten geeignet sind.
Wie dann der Text, Worte aussehen sollen, kann ich erst sagen, wenn ich das Beispiel sehe. Ich kann mir das noch nicht ganz vorstellen.
Es können gerne auch Stockbilder vorgeschlagen werden.

```html
<!DOCTYPE html>
<html lang="de">
<head>
<meta charset="utf-8">
<title>Sataya – Fury Shoals</title>
<link rel="stylesheet" href="https://fonts.googleapis.com/css2?family=Montserrat:wght@300;400&family=Permanent+Marker&display=block">
<style>
  :root {
    --red: #d8402c;
    --white: #ffffff;
    --ink: #2a2a2a;
    --paper: #ffffff;
    --sky-top: #5a4a6e;
    --sky-mid: #b58a9a;
    --sun: #f3c27a;
    --sea-dark: #1e2230;
    --boat-sky: #5f7389;
    --boat-sea: #4f7196;
    --reef-deep: #0f3f6e;
    --reef-light: #2f8a9a;
  }
  * { margin: 0; padding: 0; box-sizing: border-box; }
  html, body { width: 1200px; height: 3095px; overflow: hidden; background: var(--paper); }
  .poster { position: relative; width: 1200px; height: 3095px; background: var(--paper); overflow: hidden; font-family: "Montserrat", sans-serif; color: var(--ink); }

  .photo-sunset { position: absolute; left: 0; top: 0; width: 1200px; height: 960px;
    background: linear-gradient(180deg, var(--sky-top) 0%, var(--sky-mid) 28%, var(--sun) 46%, #7b5a63 52%, var(--sea-dark) 75%, #141620 100%); }
  .photo-boat { position: absolute; left: 0; top: 870px; width: 605px; height: 600px;
    background: linear-gradient(180deg, var(--boat-sky) 0%, #7d91a6 22%, #c9d5e0 45%, #e9eef3 55%, #8ea6bd 68%, var(--boat-sea) 100%); }
  .photo-reef { position: absolute; left: 605px; top: 870px; width: 595px; height: 600px;
    background: linear-gradient(160deg, var(--reef-deep) 0%, #1b5f8a 45%, var(--reef-light) 75%, #6fa7a0 100%); }
  .wave { position: absolute; left: 0; top: 1290px; width: 1200px; height: 180px; }

  .brand { position: absolute; right: 58px; top: 35px; width: 230px; height: 230px;
    display: flex; align-items: center; justify-content: center; text-align: center; }
  .brand-ring { position: absolute; inset: 0; }
  .brand-name { font-family: "Montserrat", sans-serif; font-weight: 400; font-size: 26px; line-height: 1.25; color: var(--white); width: 160px; }

  .title { position: absolute; left: 0; width: 1200px; text-align: center; font-family: "Permanent Marker", "Marker Felt", cursive; font-weight: 400; line-height: 1; }
  .title-main { top: 655px; font-size: 170px; color: var(--red); letter-spacing: 6px; }
  .title-region { top: 845px; font-size: 128px; color: var(--white); letter-spacing: 2px;
    text-shadow: 0 3px 12px rgba(10, 20, 35, 0.55); }

  .tagline { position: absolute; top: 1560px; left: 0; width: 1200px; text-align: center; font-size: 38px; line-height: 52px; font-weight: 400; }

  .section-heading { position: absolute; top: 1718px; left: 155px; font-family: "Permanent Marker", "Marker Felt", cursive; font-weight: 400; font-size: 78px; line-height: 1; color: var(--red); letter-spacing: 3px; }

  .boats-text { position: absolute; top: 1836px; left: 62px; width: 1085px; font-size: 32.5px; line-height: 40.6px; font-weight: 300; text-align: justify; hyphens: auto; -webkit-hyphens: auto; }
  .boats-text p { margin-bottom: 40.6px; }

  .services { position: absolute; top: 2940px; left: 0; width: 1200px; text-align: center; font-size: 41px; line-height: 52px; font-weight: 400; }
  .services .sep { color: var(--red); margin: 0 22px; }
</style>
</head>
<body>
<main class="poster">
  <div class="photo-sunset" role="img" aria-label="Foto: Sonnenuntergang über dem Roten Meer, Blick vom Deck einer Yacht mit Beiboot"></div>
  <div class="photo-boat" role="img" aria-label="Foto: Bug einer weissen Tauchsafari-Yacht auf ruhigem Wasser"></div>
  <div class="photo-reef" role="img" aria-label="Foto: Luftaufnahme einer Yacht vor dem Riff von Sataya"></div>
  <svg class="wave" viewBox="0 0 1200 180" preserveAspectRatio="none" aria-hidden="true">
    <path d="M0,95 C220,195 430,150 620,95 C820,35 1000,25 1200,55 L1200,180 L0,180 Z" fill="#ffffff"/>
  </svg>

  <div class="brand">
    <svg class="brand-ring" viewBox="0 0 230 230" aria-hidden="true">
      <circle cx="115" cy="115" r="110" fill="none" stroke="#ffffff" stroke-width="3"/>
    </svg>
    <span class="brand-name">Azurline Dive Safari</span>
  </div>

  <h1 class="title title-main">SATAYA</h1>
  <h2 class="title title-region">FURY SHOALS</h2>

  <p class="tagline">Sataya ist perfekt geeignet für Schnorcheln,<br>Tauchen und die ganze Familie</p>

  <h3 class="section-heading">BOOTE</h3>

  <div class="boats-text">
    <p>Unsere Boote Veluna und Ostrel 1, ganz auf die Bedürfnisse von Tauchern und Schnorchler abgestimmt.</p>
    <p>MY Ostrel 1 wurde 2021 gebaut. Mit einer Länge von 32 Meter und 8 Meter Breite bietet das aus Stahl konstruierte Boot bequem Platz für 24 Gäste.<br>8 Kabinen mit zwei Einzelbetten befinden sich im Unterdeck und 4 Kabinen auf dem Oberdeck.</p>
    <p>MY Veluna wurde 2019 gebaut. Mit einer Länge von 30 Metern und einer Breite von 8 Metern bietet das aus Stahl konstruierte Boot bequem Platz für 18 Gäste.<br>5 Kabinen mit zwei Einzelbetten und 2 Doppelbettkabinen befinden sich im Unterdeck und 2 Einzelbettkabinen auf dem Oberdeck.</p>
    <p>(Das folgende trifft für beide Boote zu)<br>Im Restaurant auf dem Hauptdeck werden 3 Buffets pro Tag serviert und auf dem grosszügigen Tauchdeck macht man sich für die Abenteuer bereit.<br>Auf dem Oberdeck gibt es viele schattige Sitzmöglichkeiten und eine Bar für ein gemütliches Zusammensein und zum Entspannen.<br>Auf dem Topdeck warten gemütliche Liegen, die ideal zum Sonne geniessen oder die Sterne beobachten geeignet sind.</p>
  </div>

  <p class="services">Vollcharter<span class="sep">-</span>Liveaboard<span class="sep">-</span>Mini Safari<br>Overnight<span class="sep">-</span>Tagesboot</p>
</main>
</body>
</html>
```